Construction site banner with out Company information

I need a banner 4' tall and 6' wide, I want the banner to look very similar to the photo I uploaded from LumaDraw, make the person as life like as possible, I like the eyes to pop and be blue, and the hard hat orange, with the rest black and white, I have included our logo to use on the banner as well. Include the following:
Company Name: Brelvo Staffing
Temp Employees
General and Skilled Trades
Workers Comp and Payroll Coverage
www.tmkriv.com

Target Market(s)

Construction Companies

Requirements
Nice to have
• Realistic Person, bright blue eyes, orange hard hat
Should not have
• cartoon looking person

```html
<!DOCTYPE html>
<html lang="en">
<head>
<meta charset="utf-8">
<title>Brelvo Staffing – Site Banner</title>
<link rel="stylesheet" href="https://fonts.googleapis.com/css2?family=Montserrat:wght@300;600;700&display=swap">
<style>
  :root {
    --backdrop: #e6e6e4;
    --ink-black: #050505;
    --ink-dark: #1c1c1c;
    --brand-orange: #ec5a24;
    --brand-orange-light: #f2892c;
    --paper-white: #ffffff;
  }
  * { margin: 0; padding: 0; box-sizing: border-box; }
  html, body {
    width: 1200px;
    height: 1061px;
    overflow: hidden;
    background: var(--backdrop);
    font-family: "Montserrat", Arial, sans-serif;
  }
  .banner {
    position: absolute;
    left: 0;
    top: 130px;
    width: 1200px;
    height: 800px;
    background: var(--ink-black);
    overflow: hidden;
  }
  .banner-art {
    position: absolute;
    inset: 0;
  }
  .brand-name {
    position: absolute;
    left: 56px;
    top: 78px;
    font-weight: 700;
    font-size: 92px;
    line-height: 1;
    color: var(--brand-orange-light);
    letter-spacing: -1px;
  }
  .headline {
    position: absolute;
    left: 56px;
    top: 283px;
    font-weight: 700;
    font-size: 82px;
    line-height: 86px;
    color: var(--brand-orange);
    text-transform: uppercase;
  }
  .headline .line-two { letter-spacing: 1px; }
  .tagline {
    position: absolute;
    left: 58px;
    top: 455px;
    font-weight: 700;
    font-size: 35px;
    letter-spacing: 1.5px;
    color: var(--paper-white);
    text-transform: uppercase;
  }
  .services {
    position: absolute;
    left: 58px;
    top: 608px;
    font-weight: 600;
    font-size: 42px;
    line-height: 50px;
    color: var(--ink-dark);
  }
  .services .accent { color: var(--brand-orange); }
  .web-address {
    position: absolute;
    right: 30px;
    top: 733px;
    font-weight: 300;
    font-size: 44px;
    color: var(--paper-white);
  }
  .web-address .accent { color: var(--brand-orange); }
</style>
</head>
<body>
  <section class="banner">
    <svg class="banner-art" width="1200" height="800" viewBox="0 0 1200 800">
      <defs>
        <linearGradient id="portraitTone" x1="0" y1="0" x2="0" y2="1">
          <stop offset="0" stop-color="#e0581f"/>
          <stop offset="0.22" stop-color="#8a4a2c"/>
          <stop offset="0.55" stop-color="#5a4437"/>
          <stop offset="1" stop-color="#201a17"/>
        </linearGradient>
        <linearGradient id="sceneTone" x1="0" y1="0" x2="1" y2="0">
          <stop offset="0" stop-color="#0b0b0b"/>
          <stop offset="1" stop-color="#2b2b2b"/>
        </linearGradient>
      </defs>
      <rect class="site-scene" x="327" y="0" width="400" height="800" fill="url(#sceneTone)"
            role="img" aria-label="Greyscale construction scene with a worker on a ladder"/>
      <rect class="worker-portrait" x="620" y="0" width="580" height="800" fill="url(#portraitTone)"
            role="img" aria-label="Close-up portrait of a construction worker in an orange hard hat with bright blue eyes"/>
      <path class="accent-band" d="M0 552 H450 C650 552 700 640 780 720 C820 760 860 790 907 800 H0 Z"
            fill="var(--brand-orange)"/>
      <path class="info-panel" d="M0 558 H450 C640 558 690 645 765 722 C805 762 840 790 871 800 H0 Z"
            fill="var(--paper-white)"/>
    </svg>

    <div class="brand-name">Brelvo</div>

    <h1 class="headline">
      <span class="line-one">Brelvo</span><br>
      <span class="line-two">Staffing</span>
    </h1>
    <p class="tagline">Temp Employees</p>

    <p class="services">
      <span class="accent">General and</span><br>
      <span class="accent">Skilled Trades</span> Workers<br>
      Comp and Payroll Coverage
    </p>

    <p class="web-address"><span class="accent">tmkriv</span>.com</p>
  </section>
</body>
</html>
```